Broschüre für Planungen und Verkauf von Häusern
Zielgruppe
Planungen und Verkauf von Häusern
Aufgabenstellung
Es sollte auf der Basis meines erstellten Logo und den Farben basieren. auf der vorderen Seite das Logo mit Firmennamen und
ein Spruch
Ein guter Plan heute, ist besser als ein perfekter Plan morgen
Innen aufklappbar mit zwei Laschen zum Einlegen von Angeboten usw. sowie einen Schlitz zum Einbringen von Visitenkarten
Rückseite Firmennamen Adressen Telefon usw.
Ein Beisdspiel lege ich bei, nur sollten die Farben angepasst werden

```html
<!DOCTYPE html>
<html lang="de">
<head>
<meta charset="utf-8">
<title>Broschüre – Bauvia 24 GmbH</title>
<link rel="stylesheet" href="https://fonts.googleapis.com/css2?family=Poppins:wght@400;500;600;800&display=swap">
<style>
  :root {
    --bg: #9c9c9c;
    --paper: #f8f8f8;
    --blue: #2a5ca8;
    --orange: #fdb54a;
    --dark: #303030;
    --band-grey: #e6e6e6;
    --text: #2b2b2b;
    --photo-outside: linear-gradient(180deg, #dfe8ee 0%, #cfd3d2 45%, #6f8a55 80%, #3f6d2a 100%);
    --photo-inside: linear-gradient(180deg, #e9e6dc 0%, #d8d2bf 50%, #c49d6a 100%);
  }
  * { box-sizing: border-box; margin: 0; padding: 0; }
  html, body { width: 816px; height: 1200px; overflow: hidden; }
  body {
    background: var(--bg);
    font-family: "Poppins", sans-serif;
    color: var(--text);
    display: flex;
    align-items: center;
    justify-content: center;
    gap: 20px;
  }
  .page {
    width: 356px;
    height: 503px;
    background: var(--paper);
    display: flex;
    flex-direction: column;
    box-shadow: 0 6px 14px rgba(0,0,0,.35);
  }
  .page__top { height: 186px; }
  .page__band { height: 143px; display: flex; }
  .page__dark { height: 50px; background: var(--dark); }
  .page__bottom { height: 124px; display: flex; align-items: center; }

  /* Back page */
  .back .page__band { background: var(--band-grey); align-items: center; justify-content: center; }
  .back .page__bottom { padding: 0 0 0 48px; gap: 18px; }
  .contact-title { font-weight: 800; font-size: 15px; color: var(--blue); letter-spacing: .3px; }
  .contact-list { list-style: none; font-size: 7.6px; font-weight: 500; line-height: 1.65; }
  .contact-list li { display: flex; gap: 6px; align-items: flex-start; margin-bottom: 4px; }
  .contact-list svg { flex: none; margin-top: 2px; }

  /* Wordmark */
  .wordmark {
    font-weight: 600;
    font-size: 17px;
    color: var(--blue);
    letter-spacing: .4px;
    white-space: nowrap;
  }

  /* Front page */
  .front .page__top { display: flex; flex-direction: column; align-items: center; justify-content: center; padding-top: 8px; }
  .headline { font-weight: 800; font-size: 38px; line-height: 1.02; text-align: center; letter-spacing: -.5px; }
  .headline__blue { display: block; color: var(--blue); }
  .headline__orange { display: block; color: var(--orange); }
  .tagline { margin-top: 10px; font-size: 10.6px; font-weight: 500; letter-spacing: .2px; }
  .photo { height: 100%; }
  .photo--outside { width: 124px; background: var(--photo-outside); }
  .photo--inside { width: 126px; background: var(--photo-inside); }
  .band-blue { flex: 1; background: var(--blue); }
  .front .page__bottom { justify-content: space-between; padding: 0 20px 0 20px; }
  .phone { display: flex; align-items: center; gap: 5px; font-size: 11.5px; font-weight: 500; }
</style>
</head>
<body>
  <section class="page back" aria-label="Rückseite">
    <div class="page__top"></div>
    <div class="page__band">
      <span class="wordmark">BAUVIA 24 GMBH</span>
    </div>
    <div class="page__dark"></div>
    <div class="page__bottom">
      <h2 class="contact-title">KONTAKT</h2>
      <ul class="contact-list">
        <li>
          <svg width="8" height="8" viewBox="0 0 8 8" aria-hidden="true"><rect width="8" height="8" fill="#2a5ca8"/><path d="M4 1.5a1.6 1.6 0 0 0-1.6 1.6C2.4 4.4 4 6.5 4 6.5s1.6-2.1 1.6-3.4A1.6 1.6 0 0 0 4 1.5z" fill="#fff"/><circle cx="4" cy="3.1" r=".6" fill="#2a5ca8"/></svg>
          <span>Lindenallee 24, 10115 Berlin HRB 123456<br>B GF Jonas Weber</span>
        </li>
        <li>
          <svg width="8" height="8" viewBox="0 0 8 8" aria-hidden="true"><rect width="8" height="8" fill="#2a5ca8"/></svg>
          <span>jonas-weber@beispiel-mail.de</span>
        </li>
      </ul>
    </div>
  </section>

  <section class="page front" aria-label="Vorderseite">
    <div class="page__top">
      <h1 class="headline">
        <span class="headline__blue">EIN GUTER</span>
        <span class="headline__orange">PLAN HEUTE</span>
      </h1>
      <p class="tagline">IST BESSER ALS EIN PERFEKTER PLAN MORGEN</p>
    </div>
    <div class="page__band">
      <div class="photo photo--outside" role="img" aria-label="Foto: Einfamilienhäuser mit Garten"></div>
      <div class="photo photo--inside" role="img" aria-label="Foto: heller Wohnraum mit Küche und Holzboden"></div>
      <div class="band-blue"></div>
    </div>
    <div class="page__dark"></div>
    <div class="page__bottom">
      <span class="wordmark">BAUVIA 24 GMBH</span>
      <span class="phone">
        <svg width="10" height="13" viewBox="0 0 10 13" aria-hidden="true"><path d="M2.2 0.5 3.8 3.4 2.6 4.6c.5 1.9 1.4 3.6 2.7 5l1.4-.9 2.4 2.2-1.5 1.4C4.4 11.4 1 6.9 0.6 2.2z" fill="#2b2b2b"/></svg>
        0171-555 42 80
      </span>
    </div>
  </section>
</body>
</html>
```